Welding Fabrication and Inspection Business Card Design

Welding Fabrication and Inspection Services,

Business

Industrial Machinery ServicesMohammed Rahim30 Ballarat Street, Mount Gravatt East.4122.QLD

```html
<!DOCTYPE html>
<html lang="en">
<head>
<meta charset="utf-8">
<title>Tarnwell Forge Services – Business Card</title>
<link rel="stylesheet" href="https://fonts.googleapis.com/css2?family=Arimo:wght@400;700&display=swap">
<style>
  :root {
    --card-black: #000000;
    --brand-red: #8e2f36;
    --accent-red: #b2353d;
    --icon-red: #b4484c;
    --text-white: #ffffff;
  }
  * { margin: 0; padding: 0; box-sizing: border-box; }
  html, body {
    width: 1200px;
    height: 788px;
    overflow: hidden;
    background: var(--card-black);
  }
  .card {
    position: relative;
    width: 1200px;
    height: 788px;
    background: var(--card-black);
    font-family: "Arimo", Arial, sans-serif;
    color: var(--text-white);
    overflow: hidden;
  }
  .product-photo {
    position: absolute;
    left: 97px;
    top: 46px;
    width: 351px;
    height: 282px;
    border-radius: 24px;
    background: radial-gradient(ellipse at 50% 40%, #9a3a42 0%, #5c2227 45%, #1c1c1c 75%, #000 100%);
  }
  .welding-photo {
    position: absolute;
    left: 698px;
    top: 264px;
    width: 502px;
    height: 524px;
    background:
      radial-gradient(circle at 78% 88%, #f3e7dc 0%, #d98a4a 10%, rgba(160,70,30,0.6) 28%, rgba(0,0,0,0) 55%),
      radial-gradient(ellipse at 35% 25%, rgba(90,100,112,0.7) 0%, rgba(0,0,0,0) 45%),
      linear-gradient(160deg, #000 0%, #1d1412 45%, #3a1e14 80%, #5a2c18 100%);
  }
  .brand-name {
    position: absolute;
    left: 700px;
    top: 90px;
    font-size: 56px;
    font-weight: 700;
    line-height: 1;
    color: var(--brand-red);
    white-space: nowrap;
  }
  .brand-tagline {
    position: absolute;
    left: 672px;
    top: 212px;
    font-size: 27px;
    font-weight: 700;
    letter-spacing: 0.5px;
    color: var(--text-white);
    white-space: nowrap;
  }
  .person-name {
    position: absolute;
    left: 100px;
    top: 372px;
    font-size: 37px;
    font-weight: 700;
    color: var(--text-white);
    padding-bottom: 6px;
    border-bottom: 3px solid var(--accent-red);
  }
  .contact-list {
    position: absolute;
    left: 112px;
    top: 455px;
    list-style: none;
  }
  .contact-item {
    display: flex;
    align-items: flex-start;
    font-size: 31px;
    line-height: 36px;
    margin-bottom: 18px;
    white-space: nowrap;
  }
  .contact-item svg {
    flex: none;
    width: 28px;
    height: 32px;
    margin-right: 8px;
    margin-top: 2px;
    fill: none;
    stroke: var(--icon-red);
  }
  .contact-item .solid { fill: var(--icon-red); stroke: none; }
</style>
</head>
<body>
<div class="card">
  <div class="product-photo" role="img" aria-label="Red handheld magnetic particle inspection yoke with black articulated legs"></div>
  <div class="welding-photo" role="img" aria-label="Welder in protective mask working with bright sparks flying"></div>

  <div class="brand-name">Tarnwell Forge</div>
  <div class="brand-tagline">Tarnwell Forge Services</div>

  <div class="person-name">Khalid Nasser</div>

  <ul class="contact-list">
    <li class="contact-item">
      <svg viewBox="0 0 28 32"><path class="solid" d="M6 4 l5 0 l2 7 l-3 3 q3 6 8 9 l3-3 l7 2 l0 5 q-2 3 -6 3 q-10 -2 -17 -14 q-2 -6 1 -12z"/></svg>
      <span>555-210-4417</span>
    </li>
    <li class="contact-item">
      <svg viewBox="0 0 28 32"><rect x="7" y="3" width="14" height="26" rx="2" stroke-width="2.5"/><line x1="12" y1="25" x2="16" y2="25" stroke-width="2"/></svg>
      <span>555-210-4482</span>
    </li>
    <li class="contact-item">
      <svg viewBox="0 0 28 32"><rect x="2" y="9" width="24" height="15" stroke-width="2.5"/><polyline points="2,9 14,18 26,9" stroke-width="2.5"/></svg>
      <span>khalid@tarnwellforge.com</span>
    </li>
    <li class="contact-item">
      <svg viewBox="0 0 28 32"><path class="solid" d="M14 2 a10 10 0 0 1 10 10 c0 7 -10 18 -10 18 c0 0 -10 -11 -10 -18 a10 10 0 0 1 10 -10z M14 8 a4 4 0 1 0 0.01 0z"/></svg>
      <span>17 Corrowen Street, Kellerby Heights.<br>4187.QLD</span>
    </li>
  </ul>
</div>
</body>
</html>
```